Home Staging Company needs business card design

We're a home staging company called Brightwell Harbor Home Staging. We would like a business card design that includes aqua and gray. Our current logo of house within chair is fine but I find we almost always use the logo in one color. I'll upload images of front and back of our current card and our logo. Note that we have dropped "Solutions" from our company name and don't want to include it on the card.

Target Market(s)

Realtors and homeowners - people interested in selling their homes

Contact Information for Business Card

Marisol Fenwickley
Brightwell Harbor Home Staging
757-382-6190
www.brightwellharbor.com
marisol@brightwellharbor.com

Font styles to use
Serif
Script

Requirements
Must have
• My logo and contact details
• UPDATE***
• I forgot to say that the company name should be included on the front of the card somehow.

```html
<!DOCTYPE html>
<html lang="en">
<head>
<meta charset="utf-8">
<title>Brightwell Harbor Home Staging – Business Card</title>
<link rel="stylesheet" href="https://fonts.googleapis.com/css2?family=Lora:wght@500&family=Roboto:wght@400&family=Questrial&display=swap">
<style>
  :root {
    --backdrop: #b3b3b3;
    --aqua-light: #4fb1b9;
    --aqua-deep: #1b8bb2;
    --aqua-mark: #4aa9b1;
    --card-white: #f4f4f4;
    --ink: #343434;
    --ink-soft: #4a4a4a;
    --paper-text: #ffffff;
  }
  * { box-sizing: border-box; margin: 0; padding: 0; }
  html, body {
    width: 1200px;
    height: 576px;
    overflow: hidden;
    background: var(--backdrop);
  }
  .canvas {
    position: relative;
    width: 1200px;
    height: 576px;
  }
  .card {
    position: absolute;
    top: 138px;
    width: 484px;
    height: 293px;
    border-radius: 12px;
    overflow: hidden;
  }
  /* Front side */
  .card--front {
    left: 82px;
    background: linear-gradient(180deg, var(--aqua-light) 0%, var(--aqua-deep) 100%);
    color: var(--paper-text);
  }
  .front__name {
    position: absolute;
    top: 122px;
    left: 0;
    width: 100%;
    text-align: center;
    font-family: "Lora", serif;
    font-weight: 500;
    font-size: 26px;
    letter-spacing: 0.2px;
  }
  .front__web {
    position: absolute;
    bottom: 14px;
    left: 0;
    width: 100%;
    text-align: center;
    font-family: "Questrial", sans-serif;
    font-size: 13.5px;
    letter-spacing: 0.3px;
  }
  /* Back side */
  .card--back {
    left: 602px;
    background: var(--card-white);
    color: var(--ink);
  }
  .back__accent {
    position: absolute;
    right: -58px;
    top: 12px;
    width: 270px;
    height: 270px;
    border-radius: 50%;
    background: var(--aqua-mark);
  }
  .back__company {
    position: absolute;
    top: 34px;
    left: 23px;
    font-family: "Lora", serif;
    font-weight: 500;
    font-size: 23px;
    line-height: 1.2;
    color: var(--ink);
  }
  .back__person {
    position: absolute;
    top: 168px;
    left: 23px;
  }
  .person__name {
    font-family: "Roboto", sans-serif;
    font-size: 18.5px;
    color: var(--ink);
  }
  .person__title {
    margin-top: 6px;
    font-family: "Questrial", sans-serif;
    font-size: 11px;
    color: var(--ink-soft);
  }
  .contact-list {
    position: absolute;
    top: 224px;
    left: 23px;
    list-style: none;
    font-family: "Questrial", sans-serif;
    font-size: 12.5px;
    color: var(--ink-soft);
  }
  .contact-list li {
    display: flex;
    align-items: center;
    height: 17.5px;
  }
  .contact-icon {
    width: 11px;
    height: 11px;
    margin-right: 12px;
    fill: var(--aqua-mark);
    flex: none;
  }
</style>
</head>
<body>
<main class="canvas">
  <section class="card card--front" aria-label="Card front">
    <p class="front__name">Brightwell Harbor Home Staging</p>
    <p class="front__web">www.brightwellharbor.com</p>
  </section>

  <section class="card card--back" aria-label="Card back">
    <div class="back__accent"></div>
    <p class="back__company">Brightwell Harbor<br>Home Staging</p>
    <div class="back__person">
      <p class="person__name">Marisol Fenwickley</p>
      <p class="person__title">Managing Director</p>
    </div>
    <ul class="contact-list">
      <li>
        <svg class="contact-icon" viewBox="0 0 12 12" aria-hidden="true"><path d="M1 3.5C1 2 2.5 1.5 6 1.5S11 2 11 3.5v1H8.5V3.8h-5v.7H1z"/><path d="M3 5.5h6l1.5 5h-9z"/></svg>
        757-382-6190
      </li>
      <li>
        <svg class="contact-icon" viewBox="0 0 12 12" aria-hidden="true"><circle cx="6" cy="6" r="5.2" fill="none" stroke="currentColor" style="stroke:var(--aqua-mark)" stroke-width="1.2"/><path d="M1 6h10M6 .8c-2.6 2.8-2.6 7.6 0 10.4M6 .8c2.6 2.8 2.6 7.6 0 10.4" fill="none" style="stroke:var(--aqua-mark)" stroke-width="1"/></svg>
        www.brightwellharbor.com
      </li>
      <li>
        <svg class="contact-icon" viewBox="0 0 12 12" aria-hidden="true"><path d="M1 2.5h10v7H1z"/><path d="M1.3 2.8 6 6.6l4.7-3.8" fill="none" stroke="#f4f4f4" stroke-width="1"/></svg>
        marisol@brightwellharbor.com
      </li>
    </ul>
  </section>
</main>
</body>
</html>
```